Tarrawind Music Festival needs a logo and poster design

The festival showcases West Australian bands of mixed genre from rock, pop, blues, reggae and country. It is a family friendly affair with lots of kids activities, bush camping and only 45minutes from Perth. The kookaburra and guitar neck have been the festivals motifs since inception and this year we are thinking of including the stage overhead in the design. Dates for 2024 October 11-13

```html
<!DOCTYPE html>
<html lang="en">
<head>
<meta charset="utf-8">
<title>Tarrawind Music Festival 2024</title>
<link rel="stylesheet" href="https://fonts.googleapis.com/css2?family=Bangers&family=Anton&family=Gochi+Hand&family=Oswald:wght@600&family=Poppins:wght@400;600&display=swap">
<style>
  :root {
    --ink-teal: #123a4a;
    --ink-teal-deep: #0d2f3d;
    --cream: #f7e8c9;
    --rust: #8b4a1d;
    --orange: #e07b1f;
    --gold: #f0b12c;
    --sky: #5cc0e2;
    --white: #ffffff;
    --muted: #d6e1e6;
  }
  * { box-sizing: border-box; margin: 0; padding: 0; }
  html, body { width: 695px; height: 1200px; overflow: hidden; background: var(--ink-teal-deep); }
  .poster {
    position: relative;
    width: 695px; height: 1200px;
    background: radial-gradient(ellipse at 50% 40%, #164454 0%, var(--ink-teal) 55%, var(--ink-teal-deep) 100%);
    color: var(--white);
    font-family: "Poppins", sans-serif;
    text-align: center;
  }
  .edition {
    position: absolute; top: 52px; left: 0; right: 0;
    font-family: "Bangers", cursive; font-size: 40px; letter-spacing: 4px;
    color: var(--gold);
  }
  .edition sup { font-size: 22px; vertical-align: 14px; margin-right: 18px; }
  .title {
    position: absolute; top: 96px; left: 0; right: 0;
    font-family: "Bangers", cursive; font-size: 150px; line-height: 1; letter-spacing: 2px;
    color: var(--cream);
    text-shadow: 4px 5px 0 var(--rust);
    transform: rotate(-1deg);
  }
  .illustration {
    position: absolute; top: 268px; left: 90px; width: 515px; height: 470px;
    border-radius: 48% 48% 40% 40%;
    background: radial-gradient(ellipse at 50% 45%, #e8982e 0%, #c2621d 45%, #3c6f5e 78%, rgba(18,58,74,0) 100%);
  }
  .details { position: absolute; top: 762px; left: 96px; right: 70px; height: 130px; }
  .tagline {
    position: absolute; left: 0; top: 0; text-align: left;
    font-family: "Gochi Hand", cursive; font-size: 25px; line-height: 1.05;
  }
  .tagline .white { color: var(--white); }
  .tagline .sky { color: var(--sky); }
  .tagline .gold { color: var(--gold); }
  .dates { position: absolute; right: 0; top: 34px; display: flex; align-items: flex-end; gap: 12px; }
  .dates-range {
    font-family: "Anton", sans-serif; font-size: 86px; line-height: 0.9;
    color: var(--orange); letter-spacing: -2px;
  }
  .dates-month { text-align: left; line-height: 1; }
  .dates-month .month { font-family: "Oswald", sans-serif; font-weight: 600; font-size: 46px; color: var(--cream); }
  .dates-month .year { font-family: "Poppins", sans-serif; font-size: 34px; letter-spacing: 5px; color: var(--sky); }
  .venue { position: absolute; top: 910px; left: 0; right: 0; }
  .venue .address { font-weight: 600; font-size: 14px; }
  .venue .address svg { vertical-align: -2px; margin-right: 4px; }
  .venue .drive { font-size: 14px; color: var(--gold); }
  .venue .drive span { color: var(--white); }
  .tickets { position: absolute; top: 968px; left: 0; right: 0; display: flex; justify-content: center; gap: 6px; }
  .tickets .label {
    background: var(--gold); color: var(--ink-teal); font-weight: 600; font-size: 14px;
    padding: 4px 14px;
  }
  .tickets .link {
    background: var(--cream); color: var(--ink-teal); font-weight: 600; font-size: 13px;
    padding: 5px 10px;
  }
  .charity { position: absolute; top: 1018px; left: 50px; right: 50px; font-size: 10.5px; line-height: 1.35; color: var(--muted); }
  .sponsors { position: absolute; top: 1080px; left: 0; right: 0; display: flex; justify-content: center; align-items: center; gap: 14px; }
  .sponsors .heading { font-size: 11px; letter-spacing: 4px; color: var(--muted); margin-right: 6px; }
  .sponsor { display: flex; align-items: center; gap: 4px; font-size: 10px; font-weight: 600; color: var(--white); }
  .sponsor .dot { width: 10px; height: 10px; border-radius: 50%; background: var(--gold); }
  .sponsor .square { width: 9px; height: 9px; background: var(--white); }
  .website { position: absolute; top: 1130px; left: 0; right: 0; font-size: 25px; letter-spacing: 3px; font-weight: 600; }
  .website .name { color: var(--sky); }
</style>
</head>
<body>
<main class="poster">
  <div class="edition">9<sup>TH</sup>ANNUAL</div>
  <h1 class="title">Tarrawind</h1>

  <div class="illustration" role="img" aria-label="Illustrated emblem: a kookaburra perched on an acoustic guitar beside a speaker, framed by leaves, with a Music Festival ribbon banner"></div>

  <section class="details">
    <p class="tagline">
      <span class="white">FAMILY<br>FRIENDLY AFFAIR</span><br>
      <span class="sky">WITH LOTS OF</span><br>
      <span class="white">KIDS ACTIVITIES,</span><br>
      <span class="gold">BUSH CAMPING</span>
    </p>
    <div class="dates">
      <span class="dates-range">11-13</span>
      <div class="dates-month">
        <div class="month">October</div>
        <div class="year">2024</div>
      </div>
    </div>
  </section>

  <section class="venue">
    <p class="address">
      <svg width="11" height="14" viewBox="0 0 11 14"><path d="M5.5 0C2.5 0 0 2.4 0 5.4 0 9.2 5.5 14 5.5 14S11 9.2 11 5.4C11 2.4 8.5 0 5.5 0z" fill="var(--sky)"/><circle cx="5.5" cy="5.3" r="2" fill="var(--ink-teal)"/></svg>18 BANKSIA RIDGE ROAD, MARRI HOLLOW WA 6085, AUSTRALIA
    </p>
    <p class="drive"><span>(</span>only 40mins drive from Perth<span>)</span></p>
  </section>

  <div class="tickets">
    <span class="label">GET TICKETS</span>
    <span class="link">https://tickets.eventhall.com/tarrawind-music-festival</span>
  </div>

  <p class="charity">Tarrawind Music Festival donates all profits to the Marrow Hope Foundation, local fire brigade and St Aiden's, and all volunteers and performers provide their services free of charge.</p>

  <section class="sponsors">
    <span class="heading">OUR SPONSORS</span>
    <span class="sponsor"><span class="square"></span>Ridgeline Pavers</span>
    <span class="sponsor">Kanto Civil</span>
    <span class="sponsor"><span class="dot"></span>Sunbird Audio</span>
    <span class="sponsor">Wattle Bank</span>
    <span class="sponsor">Marlo</span>
    <span class="sponsor">Halden Civil</span>
  </section>

  <p class="website">www.<span class="name">tarrawind</span>.com.au</p>
</main>
</body>
</html>
```